!! We Need YOU !! Las Vegas !! Pool Cleaning Company looking for a Brochure Design!

We are a pool/spa/water feature cleaning company for commercial properties. We are looking for a professional looking brochure to hand to clients as we speak to them about our business. We would like something that stays away from back yard pool themes like pool toys and diving boards. Our properties are resorts, hotels, casinos, and private estates so we need something to grab their attention!

Our company name is "Premier Basin Custodians"
Our slogan is "Sparkling Results"
Phone is 702-538-1726
email is rkellar@prebasincustodiansllc.example
webpage www.pre-basin-custodiansllc.example
(I know those are long! Sorry!)

We DO NOT need to include all of this in one brochure but here are some ideas for wording:

Swimming pools are a way of life in Las Vegas and PBC loves being a part of that culture. PBC is a company that has a team with 15 years of experience that spans across the Las Vegas Valley working on commercial properties. We understand the complexity of managing commercial pools and bring our resources and experience to provide you with a service that can not be matched.

the PBC advantage:
Since 2002 our team has had the privilege of providing services to resorts, casinos, hotels, and private estates. The tried and true business practices of our team have been tested and refined over the years. These practices have resulted in a set of standards to ensure PBC is a company of distinction. We believe our commitment to safety, integrity, affordability, and professionalism help us deliver the best possible pool cleaning services in Las Vegas.

Safety: PBC understands the specific requirements of the health department and chemical regulations. We work closely with the health department and exceed their requirements to help keep your property safe and compliant. PBC has developed a set of systems and programs that have been proven within the industry to accomplish reliance to safety. Our employees are dedicated to using the most advanced tools, training, and technology available to keep your property clean and safe.
Integrity:
You are secure with PBC. We pride ourselves on providing our customers with the right care for your property through honest and straightforward service. PBC will adhere to quality and honesty. PBC will have an active regard for our standards of conduct. It is our sincere belief that by establishing relationships through responsiveness to the customer's needs and dedication to our customers, that we will become the standard by which all other companies will measure their success.

Affordability: You can be assured that PBC will provide professional services at a reasonable rate. PBC will establish a long-term and beneficial relationship while fixing your costs for the next 1-5 years. We strive to keep our focus on commercial properties which means our focus is on your property. We offer exceptional pricing on cleaning, maintenance, and repair services.
Professionalism:
With any industry, you have a spectrum of professionalism. PBC strives to be at the top of that spectrum by encompassing all of the aforementioned qualities, plus many more. We strive to be the leader in providing quality service through education and certification. PBC employees always show respect for you and your property and are highly knowledgeable, courteous, and efficient. PBC will exceed expectations in the areas of accountability, customer support, and expertise.

We will be proactive rather than reactive to potentially problematic areas with proper advance planning.

When you work with PBC you can trust that our experience in the hospitality industry brings unlimited service, quick response, and a reputation to serve. If you have a commercial pool in the Las Vegas area, you should have our number.
If you are looking for knowledgeable and dependable pool cleaning and maintenance in Las Vegas, look no further than PBC.

Maintenance
▪ Regular Maintenance Services
▪ Weekly Pool/Spa Service
▪ One Time Clean-Ups
▪ DE Filter Cleaning
▪ Drain Pool & Refill
▪ Impellers
▪ Valves
▪ Algae Removal
▪ Back Wash
▪ Water Testing & Balancing
▪ Equipment Inspection
▪ Skimming, Brushing, & Leafing
Emergency service 24 hours per day, 7 days per week

Target Market(s)

High-end Resorts and properties.

Industry/Entity Type

It Company

Font styles to use
Serif
Sans Serif

Requirements
Must have
• Professional look and feel.
• Size/shape will depend on design concept-I do not care if it is traditional fold or something creative.
• Needs to have a front and back complete concept.
Nice to have
• I would like to see some ideas using our font and colors.
• I would like to focus on pictures with no buildings or beaches in them.
Should not have
• No pool toys, diving boards, palm trees, beach, or anything with a "backyard" pool feel.

```html
<!DOCTYPE html>
<html lang="en">
<head>
<meta charset="utf-8">
<title>Premier Basin Custodians – Trifold Brochure</title>
<link href="https://fonts.googleapis.com/css2?family=Lato:wght@300;400;700&family=Montserrat:wght@500;600&display=swap" rel="stylesheet">
<style>
  :root {
    --backdrop: #e9ecef;
    --sky: #5bb8e8;
    --sky-light: #7ccaf0;
    --ocean: #2f8fd3;
    --ocean-deep: #1f6fbf;
    --navy: #1a4f96;
    --white: #ffffff;
    --paper: #f7fbfe;
    --photo-water: #3aa6d6;
    --photo-sky: #b8d9ee;
    --photo-dark: #24333c;
    --photo-green: #6f9a4a;
  }
  * { box-sizing: border-box; margin: 0; padding: 0; }
  html, body { width: 1200px; height: 638px; overflow: hidden; }
  body {
    background: var(--backdrop);
    font-family: "Lato", Arial, sans-serif;
    color: var(--white);
    position: relative;
  }
  .brochure {
    position: absolute;
    left: 105px; top: 24px;
    width: 990px; height: 590px;
    display: flex;
    box-shadow: 0 6px 20px rgba(0,0,0,.18);
  }
  .panel { position: relative; width: 330px; height: 590px; overflow: hidden; }

  /* Left panel – services */
  .panel--services {
    background: linear-gradient(180deg, var(--sky-light) 0%, var(--sky) 45%, var(--ocean) 100%);
  }
  .services__band {
    position: absolute; left: 0; top: 0; width: 100%; height: 110px;
    background: rgba(255,255,255,.12);
  }
  .services__title {
    position: absolute; left: 34px; top: 120px;
    font-family: "Montserrat", Arial, sans-serif; font-weight: 600;
    font-size: 24px;
  }
  .services__list {
    position: absolute; left: 34px; top: 162px;
    list-style: none; font-weight: 300; font-size: 14px; line-height: 19px;
  }
  .services__note {
    position: absolute; left: 34px; top: 408px; width: 260px;
    font-weight: 300; font-size: 14px; line-height: 19px;
  }
  .services__photo {
    position: absolute; left: 30px; top: 455px;
    width: 270px; height: 270px; border-radius: 50%;
    border: 10px solid var(--ocean-deep);
    background: radial-gradient(circle at 40% 40%, #e9ecea 0%, var(--photo-green) 38%, var(--photo-dark) 75%);
  }

  /* Middle panel – contact */
  .panel--contact {
    background: linear-gradient(180deg, var(--ocean) 0%, var(--sky) 100%);
  }
  .brand {
    display: flex; align-items: center; gap: 10px;
  }
  .brand__dot { width: 26px; height: 26px; border-radius: 50%; background: var(--white); flex: none; }
  .brand__name { font-weight: 700; font-size: 40px; letter-spacing: 1px; line-height: 1; }
  .brand__full { font-weight: 400; font-size: 8px; letter-spacing: 1.6px; text-transform: uppercase; margin-top: 3px; }
  .contact__brand { position: absolute; left: 54px; top: 70px; color: var(--white); }
  .contact__band {
    position: absolute; left: 0; top: 178px; width: 100%; height: 200px;
    background: var(--ocean-deep);
    text-align: center;
  }
  .contact__slogan { margin-top: 22px; font-size: 13px; }
  .contact__icon { margin: 12px auto 6px; width: 48px; height: 48px; display: block; }
  .contact__phone { font-weight: 700; font-size: 34px; letter-spacing: 1px; }
  .contact__line { font-size: 10.5px; font-weight: 400; line-height: 15px; }
  .contact__line:first-of-type { margin-top: 8px; }

  /* Right panel – cover */
  .panel--cover { background: var(--paper); }
  .cover__brand { position: absolute; left: 44px; top: 40px; color: var(--ocean-deep); }
  .cover__photo {
    position: absolute; left: 0; top: 140px; width: 100%; height: 450px;
    background: linear-gradient(180deg, var(--photo-sky) 0%, #dfe9ef 38%, var(--photo-water) 58%, #1d7fb8 100%);
  }
  .cover__swoosh { position: absolute; left: 0; top: 0; width: 100%; height: 590px; }
  .cover__text { position: absolute; right: 22px; top: 420px; text-align: right; }
  .cover__title { font-size: 25px; font-weight: 400; line-height: 30px; }
  .cover__slogan { font-size: 13px; font-weight: 700; margin-top: 6px; }
  .cover__web { font-size: 9px; margin-top: 8px; }
</style>
</head>
<body>
<div class="brochure">

  <section class="panel panel--services">
    <div class="services__band"></div>
    <h2 class="services__title">Maintenance</h2>
    <ul class="services__list">
      <li>Regular Maintenance Services</li>
      <li>Weekly Pool/Spa Service</li>
      <li>One Time Clean-Ups</li>
      <li>DE Filter Cleaning</li>
      <li>Drain Pool &amp; Refill</li>
      <li>Impellers</li>
      <li>Valves</li>
      <li>Algae Removal</li>
      <li>Back Wash</li>
      <li>Water Testing &amp; Balancing</li>
      <li>Equipment Inspection</li>
      <li>Skimming, Brushing, &amp; Leafing</li>
    </ul>
    <p class="services__note">Emergency service 24 hours per day, 7 days per week.</p>
    <div class="services__photo" role="img" aria-label="Spa still life photo: white orchid, rolled green towel, candle and bamboo stalks on dark stones"></div>
  </section>

  <section class="panel panel--contact">
    <div class="contact__brand">
      <div class="brand"><span class="brand__dot"></span><span class="brand__name">PBC</span></div>
      <div class="brand__full">Premier Basin Custodians</div>
    </div>
    <div class="contact__band">
      <p class="contact__slogan">Sparkling Results</p>
      <svg class="contact__icon" viewBox="0 0 48 48" aria-hidden="true">
        <circle cx="24" cy="24" r="21" fill="none" stroke="#fff" stroke-width="3"/>
        <path d="M17 14c1.5-1 3-.5 3.8 1l1.6 3c.6 1.2.2 2.3-.8 3l-1 .8c.9 2.4 2.8 4.4 5.2 5.4l.9-1c.8-.9 2-1.2 3.1-.6l3 1.6c1.4.8 1.8 2.4.8 3.8-1.6 2.3-4 3-6.6 2-5.4-2-9.5-6.1-11.4-11.5-.9-2.6-.1-5 1.4-6.5z" fill="#fff"/>
      </svg>
      <p class="contact__phone">702-538-1726</p>
      <p class="contact__line">rkellar@prebasincustodiansllc.example</p>
      <p class="contact__line">www.pre-basin-custodiansllc.example</p>
    </div>
  </section>

  <section class="panel panel--cover">
    <div class="cover__brand">
      <div class="brand"><span class="brand__dot" style="background:var(--ocean-deep)"></span><span class="brand__name">PBC</span></div>
      <div class="brand__full">Premier Basin Custodians</div>
    </div>
    <div class="cover__photo" role="img" aria-label="Resort pool deck photo: white parasols and lounge chairs beside a blue pool under a clear sky"></div>
    <svg class="cover__swoosh" viewBox="0 0 330 590" preserveAspectRatio="none" aria-hidden="true">
      <path d="M0 0 H28 C18 200 60 420 150 590 H0 Z" fill="var(--ocean)"/>
      <path d="M28 0 C18 200 60 420 150 590 H128 C46 420 8 200 16 0 Z" fill="var(--navy)"/>
    </svg>
    <div class="cover__text">
      <p class="cover__title">Premier Basin<br>Custodians™</p>
      <p class="cover__slogan">Our slogan is "Sparkling Results"</p>
      <p class="cover__web">www.pre-basin-custodiansllc.example</p>
    </div>
  </section>

</div>
</body>
</html>
```